We need an eye catching logo design and Business Card that portrays our business, which is the cleaning and protecting of stainless steel with an organic non chemical product. This can be separate to the company name or can incorporate it. Maybe even just the company name itself. Company Name is Gleamwise Gleamwise.
Ideal for products exposed to weather elements, ie: balustrading, enclosures, BBQs, we also supply the product so you can do it yourself (DIY).
In addition we would want to include on this card:
1. My Name (Paul Dremmick)
2. Mobile No. (TBA Later)
3. Email address (TBA Later)
4. Web address (TBA Later)
Updates

Please note that we also need suggestions on a logo, as this we do not have this either.

Please note we have update our brief to be more specific.

Thank You.

Paul

Reason: Awaiting for a couple of revised submissions from feedback given.

Target Market(s)

Purchasing officers and government people.

Industry/Entity Type

Steel

Colors

Designer to choose colors to be used in the design.

Requirements
Must have
• 1. Name (Paul Dremmick)
2. Mobile No. (TBA Later)
Should not have
• Should not be to busy looking

```html
<!DOCTYPE html>
<html lang="en">
<head>
<meta charset="utf-8">
<title>Gleamwise Gleamwise – Business Card</title>
<link href="https://fonts.googleapis.com/css2?family=Fira+Sans:wght@400;600;700&display=swap" rel="stylesheet">
<style>
  :root {
    --backdrop-top: #e4e4e4;
    --backdrop-bottom: #c9c9c9;
    --steel-light: #f4f4f4;
    --steel-mid: #d8d8d8;
    --steel-dark: #bdbdbd;
    --ink-soft: #8a8a8a;
    --ink-body: #555555;
    --ink-strong: #3a3a3a;
    --ink-logo: #2f2f2f;
  }
  * { margin: 0; padding: 0; box-sizing: border-box; }
  html, body {
    width: 1200px;
    height: 861px;
    overflow: hidden;
  }
  body {
    background: linear-gradient(180deg, var(--backdrop-top), var(--backdrop-bottom));
    font-family: "Fira Sans", Arial, sans-serif;
    position: relative;
  }
  .card {
    position: absolute;
    top: 288px;
    width: 500px;
    height: 286px;
    border-radius: 3px;
    background: linear-gradient(125deg, var(--steel-dark) 0%, var(--steel-light) 42%, var(--steel-mid) 70%, var(--steel-light) 100%);
    box-shadow: 0 10px 24px rgba(0,0,0,0.18), 0 2px 4px rgba(0,0,0,0.12);
    overflow: hidden;
  }
  .card--front { left: 60px; }
  .card--back { left: 640px; }

  .contact {
    position: absolute;
    left: 40px;
    top: 92px;
    color: var(--ink-body);
  }
  .contact__name {
    font-size: 34px;
    font-weight: 700;
    color: var(--ink-soft);
    line-height: 1;
  }
  .contact__position {
    font-size: 17px;
    font-weight: 400;
    color: var(--ink-body);
    letter-spacing: 0.5px;
    margin-top: 4px;
  }
  .contact__list {
    list-style: none;
    margin-top: 18px;
    font-size: 16px;
    line-height: 1.45;
  }
  .contact__label {
    font-weight: 700;
    color: var(--ink-strong);
  }

  .brand {
    position: absolute;
    left: 0;
    right: 0;
    top: 0;
    bottom: 0;
    display: flex;
    flex-direction: column;
    justify-content: center;
    padding-left: 70px;
    color: var(--ink-logo);
    font-size: 50px;
    font-weight: 700;
    line-height: 1.05;
    text-transform: uppercase;
    letter-spacing: 1px;
  }
</style>
</head>
<body>
  <section class="card card--front" aria-label="Business card front">
    <div class="contact">
      <h1 class="contact__name">Paul Dremmick</h1>
      <p class="contact__position">POSITION</p>
      <ul class="contact__list">
        <li><span class="contact__label">Mobile:</span> 1234567890</li>
        <li><span class="contact__label">E-mail:</span> yourname@domain.com</li>
        <li><span class="contact__label">Website:</span> yourcompany.com</li>
      </ul>
    </div>
  </section>

  <section class="card card--back" aria-label="Business card back">
    <p class="brand"><span>Gleamwise</span><span>Gleamwise</span></p>
  </section>
</body>
</html>
```